Tourism Marketing needing sleek, clear design for business card & proposal documents.

***Company background***
"Quiet Harbour" is a company specializing in tourism marketing and project management. We do international wholesale, event management as well as ongoing representation of tourism and hospitality companies.

***Target market***
We cater to tourism companies and hotel professionals.

***Task***
We would like to get a single sided business card designed (but will still consider two sided, we are open to any ideas you may have). The layout for this card should be modern and elegant. Currently we do not have a logo, but we would like our business name in a really simple typography for the business card (similar to Moonrise Palace's logo - www.moonrisepalace-example.com.au).We are after a design that is clear, strong enough to be recognised as Quiet Harbour that does not require any fancy design. Another option is a simple play on QH (Quiet Harbour) or simply have Quiet Harbour featured elsewhere on card more as a brand/logo.

Feel free to submit different fonts if you feel you have any other fonts/designs that may be suitable for this card other than sans serifs. Should this project be successful, we will be considering several other projects for business proposal templates and eventually a website design.

The information that needs to go on the card are as follows:

Marta Holloway
Director
Quiet Harbour
Tourism Marketing & Representation
87 Wendover Parade
Prahran, Victoria, 3181 Australia
T +61 498203617 E marta@quietharbour-example.com.au

***Look and feel***
We'd like the business card design to express the following:
Modern, sleek, elegant, simple, discreet, quality, subtle, professional, creative, innovation

In terms of typography, we like something really simple and blocky (similar font to Moonrise Palace's logo - www.moonrisepalace-example.com.au)

***Colour scheme***
Shades of grey and dark teal

***Note***
Although our main target market are professionals, we would like the business card design to be versatile enough to be used outside of the tourism industry and need to appeal to different markets.

I do not have existing logo. Was hoping for a design that may be clear, strong enough not to require one. Other option is a simple play on QH (Quiet Harbour) or simply have Quiet Harbour featured elsewhere on card more as a brand/logo.

Marta Holloway
Director
Quiet Harbour Pty Ltd 
87 Wendover Parade
T +61 498203617  E  marta@quietharbour-example.com.au

Thank you for designs so far. Many have used a mauve colour which matches our company profile. This is not necessary, as that is just a draft and will be completely redesigned, so dont  feel you need to incorporate the mauve.

My colour preferences are for a white or grey background, and I like fonts in dark teals, grey or other sophisticated but modern colours. feel free to submit different fonts if you you have other fonts you thing would be suitable for this card, along with sans serifs. Should this project be successful, we will be considering several others for business proposal templates and eventually website. 

Target Market(s)

International Hospitality Senior Executives, Directors of International Tourism Companies, Directors of Tourism Bodies Internationally, local Tourism

Industry/Entity Type

Hospitality

Requirements
Should not have
• must not have bright garish colour, swirly patterns or anything that dates too much.

```html
<!DOCTYPE html>
<html lang="en">
<head>
<meta charset="utf-8">
<title>Quiet Harbour — Business Card</title>
<link rel="stylesheet" href="https://fonts.googleapis.com/css2?family=Tinos:wght@400;700&display=swap">
<style>
  :root {
    --backdrop: #4a4847;
    --card-stone: #b3b1a4;
    --card-mist: #cdccc3;
    --photo-warm: #d6d3c7;
    --photo-sea: #bfc3bd;
    --photo-shade: #a9a79a;
    --ink: #141414;
    --ink-soft: #2a2a2a;
  }
  * { margin: 0; padding: 0; box-sizing: border-box; }
  html, body { width: 1200px; height: 900px; overflow: hidden; }
  body {
    background: var(--backdrop);
    font-family: "Tinos", "Times New Roman", serif;
    color: var(--ink);
    position: relative;
  }
  .card {
    position: absolute;
    top: 300px;
    width: 525px;
    height: 300px;
    border-radius: 18px;
    overflow: hidden;
  }
  .card--front { left: 58px; background: var(--card-stone); }
  .card--back { left: 617px; background: var(--card-mist); }

  .wordmark {
    font-weight: 400;
    color: var(--ink);
    white-space: nowrap;
    letter-spacing: 0.02em;
  }
  .card--front .wordmark {
    position: absolute;
    left: 0; right: 0;
    top: 112px;
    text-align: center;
    font-size: 50px;
    line-height: 1;
  }
  .card--front .web {
    position: absolute;
    left: 0; right: 0;
    top: 210px;
    text-align: center;
    font-size: 16px;
    letter-spacing: 0.08em;
    color: var(--ink-soft);
  }

  .backdrop-photo {
    position: absolute;
    inset: 0;
    background:
      linear-gradient(180deg, rgba(214,211,199,0.0) 0%, rgba(169,167,154,0.35) 100%),
      linear-gradient(90deg, var(--photo-sea) 0%, var(--photo-warm) 45%, var(--photo-sea) 60%, var(--photo-shade) 100%);
    opacity: 0.75;
  }
  .card--back .wordmark {
    position: absolute;
    left: 30px;
    top: 52px;
    font-size: 36px;
    line-height: 1;
  }
  .contact {
    position: absolute;
    left: 47px;
    top: 130px;
    font-size: 12.5px;
    line-height: 13px;
    color: var(--ink-soft);
  }
  .contact .name { font-weight: 700; font-size: 15px; letter-spacing: 0.04em; color: var(--ink); line-height: 16px; }
  .contact .group { margin-bottom: 14px; }
  .contact .company { font-size: 14px; line-height: 15px; }
  .contact .lines { font-size: 12.5px; }
  .contact .reach { font-size: 13px; word-spacing: 1px; }
</style>
</head>
<body>
  <section class="card card--front">
    <div class="wordmark">Quiet Harbour</div>
    <div class="web">www.quietharbour-example.com.au</div>
  </section>

  <section class="card card--back">
    <div class="backdrop-photo" role="img" aria-label="Faded photograph of a bright resort lounge opening onto a sea view with islands"></div>
    <div class="wordmark">Quiet Harbour</div>
    <div class="contact">
      <div class="group">
        <div class="name">Marta Holloway</div>
        <div class="lines">Director</div>
      </div>
      <div class="group">
        <div class="company">Quiet Harbour Pty Ltd</div>
        <div class="lines">Tourism Marketing &amp; Representation</div>
      </div>
      <div class="group">
        <div class="lines">87 Wendover Parade</div>
        <div class="lines">Prahran, Victoria, 3181 Australia</div>
      </div>
      <div class="reach">T: +61 498203617&nbsp; E:&nbsp; marta@quietharbour-example.com.au</div>
    </div>
  </section>
</body>
</html>
```